KRT-VB 2018 Recycling Rate Report

We need a design for our 2018 Recycling Rate Report on Expanded Polystyrene. We want to move from a larger booklet style to a two page document. The report from last year - which was done as a booklet - is attached to provide an example of our style and design.The primary items that must be included (but not limited to) the information on pages 3, 5 & 7. The graphs must include room for 2018 data.To view our typical company design/style please see our website at www.kortavale.org. Our primary RGB colors are: (187,140,9); (94,47,29); (94,138,164); and (164,167,15). Secondary RGB colors are (249,162,28) and (218,210,208). Our title/header font is DIN Next LT Pro and our copy font is Calibri 10.5 pt. We can deviate from the font specification if beneficial and welcome interesting text treatments and typography.

Target Market(s)

Recycling facilities & general public.

Font styles to use
Sans Serif

Requirements
Must have
• Information presentation must be clean and easy to reference.

```html
<!DOCTYPE html>
<html lang="en">
<head>
<meta charset="utf-8">
<title>KRT-VB 2018 Recycling Rate Report</title>
<link rel="stylesheet" href="https://fonts.googleapis.com/css2?family=Barlow+Semi+Condensed:wght@300;400;600;700&family=Carlito:wght@400;700&display=swap">
<style>
  :root{
    --gold:#bb8c09;
    --gold-dark:#8a6707;
    --brown:#5e2f1d;
    --blue:#5e8aa4;
    --olive:#a4a70f;
    --olive-dark:#7d7f0b;
    --orange:#f9a21c;
    --stone:#dad2d0;
    --ink:#222;
    --grid:#e4e4e4;
    --head:"Barlow Semi Condensed", sans-serif;
    --copy:"Carlito", sans-serif;
  }
  *{box-sizing:border-box;margin:0;padding:0}
  html,body{width:1200px;height:1200px;overflow:hidden}
  body{background:#ececec;position:relative;font-family:var(--copy);color:var(--ink)}
  .page{position:absolute;left:160px;width:880px;height:570px;background:#fff;overflow:hidden;box-shadow:0 2px 8px rgba(0,0,0,.12)}
  .cover{top:20px}
  .spread{top:610px}
  .abs{position:absolute}

  /* cover */
  .bead-photo{position:absolute;inset:0;background:
    radial-gradient(ellipse 70% 40% at 70% 8%, #ffffff 0%, #f2f2f2 55%, transparent 80%),
    linear-gradient(180deg,#ededed 0%,#e6e6e6 60%,#dedede 100%)}
  .brand{position:absolute;left:26px;top:21px;display:flex;align-items:center;gap:8px}
  .brand-dot{width:90px;height:90px;border-radius:50%;background:var(--gold)}
  .brand-name{font-family:var(--head);font-weight:400;color:var(--gold);font-size:20px;line-height:18px}
  .headline{position:absolute;right:323px;text-align:right;font-family:var(--head);white-space:nowrap}
  .headline.light{font-weight:300;color:var(--gold);font-size:60px;line-height:1}
  .headline.strong{font-weight:700;color:var(--olive);font-size:64px;line-height:1;letter-spacing:-.5px}
  .ribbon-year{position:absolute;left:612px;top:328px;font-family:var(--head);font-weight:700;color:#fff;font-size:80px;line-height:1;letter-spacing:2px}
  .ribbon-label{position:absolute;left:607px;top:432px;font-family:var(--head);font-weight:700;color:#fff;font-size:16px;line-height:19px}

  /* spread */
  .sidebar-text{position:absolute;left:21px;top:36px;width:126px;color:#fff}
  .sidebar-text h2{font-family:var(--head);font-weight:700;font-size:16px;line-height:17px;margin-bottom:4px}
  .sidebar-text p{font-size:5.6px;line-height:6.9px;text-align:justify;text-indent:4px;margin-bottom:3px}
  .sidebar-text h2.second{margin-top:12px}
  .mini-brand{position:absolute;left:37px;top:517px;display:flex;align-items:center;gap:4px}
  .mini-brand .brand-dot{width:30px;height:30px}
  .mini-brand .brand-name{font-size:9px;line-height:8.5px}
  .band{position:absolute;top:2px;height:42px;color:#fff;font-family:var(--head);font-weight:700;display:flex;align-items:center;justify-content:center;font-size:17px;letter-spacing:.3px}
  .band.orange{left:162px;width:584px;width:422px;background:var(--orange)}
  .band.olive{left:584px;width:292px;background:var(--olive)}
  .photo-round{position:absolute;border-radius:50%;width:82px;height:82px}
  .photo-sorting{left:178px;top:59px;background:radial-gradient(circle at 40% 45%,#cfd6dc,#5b6670 70%,#2f353a)}
  .photo-worker{left:484px;top:59px;background:radial-gradient(circle at 55% 50%,#e6eaf0,#7c8fa3 65%,#3b4a5a)}
  .photo-beads{left:607px;top:60px;background:radial-gradient(circle at 45% 45%,#fbfbfb,#e3e3e3 70%,#cfcfcf)}
  .stat{position:absolute;text-align:center;font-family:var(--head)}
  .stat .label{font-size:15px;font-weight:400;color:#222;line-height:1}
  .stat .unit{font-family:var(--copy);font-size:6.5px;color:#444;margin-top:2px}
  .stat .value{font-size:36px;font-weight:700;line-height:1;margin-top:3px}
  .stat.industrial{left:256px;top:73px;width:120px}
  .stat.industrial .value{color:var(--orange)}
  .stat.consumer{left:372px;top:73px;width:120px}
  .stat.consumer .value{color:var(--olive)}
  .stat-divider{position:absolute;left:374px;top:70px;height:67px;border-left:1px dotted #c9c9c9}
  .pill{position:absolute;border-radius:30px;background:var(--olive);color:#fff;display:flex;align-items:center}
  .pill p{font-size:5.8px;line-height:7.2px;text-align:justify}
  .pill-history{left:178px;top:336px;width:388px;height:45px;padding:0 24px 0 58px}
  .pill-outlook{left:599px;top:398px;width:257px;height:75px;padding:0 14px 0 48px}
  .pill svg{position:absolute;left:18px;top:50%;transform:translateY(-50%)}
  .pill-outlook svg{left:12px}
  .contact-box{position:absolute;left:178px;top:411px;width:388px;height:136px;border:1.5px dotted #d8d39a;border-radius:26px;text-align:center}
  .contact-box h3{font-family:var(--copy);font-weight:700;font-size:11px;margin-top:18px}
  .contact-box .fine{font-size:5.8px;line-height:7.5px;color:#333}
  .contact-line{display:flex;align-items:center;justify-content:center;gap:6px;margin-top:8px;font-weight:700;font-size:6px}
  .contact-line.phone{font-size:10px}
  .social-square{width:9px;height:9px;border-radius:2px;background:var(--olive)}
  .data-text{position:absolute;left:690px;top:58px;width:174px;font-size:5.9px;line-height:7.1px;text-align:right}
  .total{position:absolute;right:16px;top:155px;display:flex;align-items:flex-end;gap:8px}
  .total .caption{text-align:right;font-family:var(--head);font-size:14px;line-height:1}
  .total .caption small{display:block;font-family:var(--copy);font-size:6px;margin-top:1px}
  .total .num{font-family:var(--head);font-weight:700;font-size:38px;color:var(--orange);line-height:.9;padding-left:8px;border-left:1px dotted #c9c9c9}
  .bar-title{position:absolute;left:599px;width:276px;top:223px;text-align:center;font-family:var(--head);font-weight:600;font-size:12px;line-height:1}
  .bar-title small{display:block;font-family:var(--copy);font-weight:400;font-size:6.5px;margin-top:3px}
  .legend{position:absolute;top:366px;display:flex;align-items:center;gap:4px;font-size:5.5px;font-weight:700;letter-spacing:.2px}
  .legend i{display:block;width:20px;height:20px;border-radius:50%}
  .legend.consumer{left:637px}
  .legend.consumer i{background:var(--olive)}
  .legend.industrial{left:732px}
  .legend.industrial i{background:var(--orange)}
  .column-rule{position:absolute;left:585px;top:58px;height:432px;border-left:1px dotted #cfcfcf}
  .footer-tag{position:absolute;right:15px;top:537px;font-family:var(--head);font-weight:700;font-size:10.5px;color:var(--olive)}
  .footer-tag b{color:var(--gold)}
  .chart{position:absolute;left:0;top:0}
</style>
</head>
<body>

<section class="page cover">
  <div class="bead-photo" role="img" aria-label="Close-up photo of white expanded polystyrene beads scattered across a light surface"></div>
  <div class="brand"><span class="brand-dot"></span><span class="brand-name">Kortavale<br>Alliance</span></div>

  <div class="headline light" style="top:314px">TAKE</div>
  <div class="headline light" style="top:375px">A LOOK AT</div>
  <div class="headline strong" style="top:428px">EPS RECYCLING</div>

  <svg class="chart" width="880" height="570" viewBox="0 0 880 570" aria-hidden="true">
    <polygon points="577,312 857,312 822,364 857,416 577,416" fill="var(--gold)"/>
    <rect x="577" y="312" width="20" height="104" fill="var(--gold-dark)"/>
    <polygon points="577,424 787,424 762,450 787,476 577,476" fill="var(--olive)"/>
    <rect x="577" y="424" width="9" height="52" fill="var(--olive-dark)"/>
  </svg>
  <div class="ribbon-year">2018</div>
  <div class="ribbon-label">EPS RECYCLING<br>RATE REPORT</div>
</section>

<section class="page spread">
  <svg class="chart" width="880" height="570" viewBox="0 0 880 570">
    <polygon points="4,2 162,2 162,492 83,470 4,492" fill="var(--olive)"/>

    <!-- line chart -->
    <g font-family="Carlito, sans-serif" font-size="5" fill="#333">
      <g stroke="var(--grid)" stroke-width=".7">
        <line x1="213" y1="168" x2="213" y2="310"/><line x1="237.4" y1="168" x2="237.4" y2="310"/>
        <line x1="261.9" y1="168" x2="261.9" y2="310"/><line x1="286.3" y1="168" x2="286.3" y2="310"/>
        <line x1="310.7" y1="168" x2="310.7" y2="310"/><line x1="335.2" y1="168" x2="335.2" y2="310"/>
        <line x1="359.6" y1="168" x2="359.6" y2="310"/><line x1="384" y1="168" x2="384" y2="310"/>
        <line x1="408.4" y1="168" x2="408.4" y2="310"/><line x1="432.9" y1="168" x2="432.9" y2="310"/>
        <line x1="457.3" y1="168" x2="457.3" y2="310"/><line x1="481.7" y1="168" x2="481.7" y2="310"/>
        <line x1="506.2" y1="168" x2="506.2" y2="310"/><line x1="530.6" y1="168" x2="530.6" y2="310"/>
        <line x1="555" y1="168" x2="555" y2="310"/>
      </g>
      <g text-anchor="end">
        <text x="203" y="312">0</text><text x="203" y="292">10</text><text x="203" y="271">20</text>
        <text x="203" y="251">30</text><text x="203" y="231">40</text><text x="203" y="210">50</text>
        <text x="203" y="190">60</text><text x="203" y="170">70</text>
      </g>
      <text transform="translate(182 240) rotate(-90)" text-anchor="middle" font-size="4.5" fill="#666">Millions of Pounds Recycled</text>
      <polyline fill="none" stroke="var(--gold)" stroke-width="1.2"
        points="213,303.9 237.4,267.8 261.9,260.9 286.3,264.3 310.7,273.1 335.2,259.5 359.6,256.8 384,259.3 408.4,245 432.9,241.8 457.3,234.7 481.7,235.5 506.2,182.1 530.6,257.4 555,249.1"/>
      <g fill="var(--orange)">
        <circle cx="213" cy="303.9" r="1.8"/><circle cx="237.4" cy="267.8" r="1.8"/><circle cx="261.9" cy="260.9" r="1.8"/>
        <circle cx="286.3" cy="264.3" r="1.8"/><circle cx="310.7" cy="273.1" r="1.8"/><circle cx="335.2" cy="259.5" r="1.8"/>
        <circle cx="359.6" cy="256.8" r="1.8"/><circle cx="384" cy="259.3" r="1.8"/><circle cx="408.4" cy="245" r="1.8"/>
        <circle cx="432.9" cy="241.8" r="1.8"/><circle cx="457.3" cy="234.7" r="1.8"/><circle cx="481.7" cy="235.5" r="1.8"/>
        <circle cx="506.2" cy="182.1" r="2.2"/><circle cx="530.6" cy="257.4" r="1.8"/><circle cx="555" cy="249.1" r="3.5"/>
      </g>
      <g text-anchor="middle">
        <text x="213" y="297">3.0</text><text x="237.4" y="261">20.8</text><text x="261.9" y="254">24.2</text>
        <text x="286.3" y="258">22.5</text><text x="310.7" y="283">18.2</text><text x="335.2" y="253">24.9</text>
        <text x="359.6" y="250">26.2</text><text x="384" y="253">25.0</text><text x="408.4" y="238">32.0</text>
        <text x="432.9" y="235">33.6</text><text x="457.3" y="228">37.1</text><text x="481.7" y="229">36.7</text>
        <text x="506.2" y="176">63.0</text><text x="530.6" y="267">25.9</text><text x="558" y="259">30.0</text>
      </g>
      <g text-anchor="middle" font-size="4.6">
        <text x="213" y="322">1990</text><text x="237.4" y="322">1992</text><text x="261.9" y="322">1994</text>
        <text x="286.3" y="322">1996</text><text x="310.7" y="322">1998</text><text x="335.2" y="322">2000</text>
        <text x="359.6" y="322">2002</text><text x="384" y="322">2004</text><text x="408.4" y="322">2006</text>
        <text x="432.9" y="322">2008</text><text x="457.3" y="322">2010</text><text x="481.7" y="322">2012</text>
        <text x="506.2" y="322">2016</text><text x="530.6" y="322">2017</text><text x="555" y="322">2018</text>
      </g>
    </g>

    <!-- bar chart -->
    <g font-family="Carlito, sans-serif" font-size="3.6" text-anchor="middle">
      <line x1="600" y1="350.5" x2="855" y2="350.5" stroke="#bbb" stroke-width=".6"/>
      <g fill="var(--olive)">
        <rect x="603" y="317" width="12" height="33"/><rect x="639" y="315.5" width="12" height="34.5"/>
        <rect x="674" y="301" width="12" height="49"/><rect x="710" y="299" width="12" height="51"/>
        <rect x="749" y="263" width="12" height="87"/><rect x="785" y="314" width="12" height="36"/>
        <rect x="822" y="308.5" width="12" height="41.5"/>
      </g>
      <g fill="var(--orange)">
        <rect x="616" y="328.5" width="12" height="21.5"/><rect x="652" y="306" width="12" height="44"/>
        <rect x="687" y="299" width="12" height="51"/><rect x="723" y="273" width="12" height="77"/>
        <rect x="762" y="273" width="12" height="77"/><rect x="798" y="294.5" width="12" height="55.5"/>
        <rect x="835" y="296" width="12" height="54"/>
      </g>
      <g fill="var(--olive)">
        <text x="609" y="315">24.0</text><text x="645" y="313.5">25.0</text><text x="680" y="299">35.6</text>
        <text x="716" y="297">36.7</text><text x="755" y="261">63.0</text><text x="791" y="312">25.9</text><text x="828" y="306.5">30.0</text>
      </g>
      <g fill="var(--orange)">
        <text x="622" y="326.5">15.6</text><text x="658" y="304">32.0</text><text x="693" y="297">37.0</text>
        <text x="729" y="271">56.0</text><text x="768" y="271">56.0</text><text x="804" y="292.5">40.2</text><text x="841" y="294">39.0</text>
      </g>
      <g fill="#333" font-weight="700">
        <text x="616" y="357">2000</text><text x="652" y="357">2004</text><text x="687" y="357">2008</text>
        <text x="723" y="357">2012</text><text x="762" y="357">2016</text><text x="798" y="357">2017</text><text x="835" y="357">2018</text>
      </g>
    </g>
  </svg>

  <div class="sidebar-text">
    <h2>METHODOLOGY</h2>
    <p>The 2017 Expanded Polystyrene Recycling Rate Study was conducted by the Kortavale Alliance to gather data to reflect both post-consumer and post-industrial recycling activity. The 2017 results are based on data received from 55 EPS manufacturers and independent recyclers in the U.S.</p>
    <p>Participation in the EPS recycling survey is voluntary and the reported data is based on the responses received. Many companies have limited resources to put towards participation in the survey, and some companies may choose not to respond due to their confidentiality policies. Therefore, because there is not 100 percent participation, the presented totals represent the minimum amount of EPS recovered for recycling.</p>
    <h2 class="second">COLLECTION<br>OPTIONS &amp;<br>RESOURCES</h2>
    <p>Not everything can be recycled all the time. In order for materials to be recycled, stable markets must exist and there must be a demand for the end products. Each community has its own guidelines for which plastics are accepted, and these can vary widely. Some locations also offer consumer drop-off access. To find out if EPS recycling is available in your area, visit www.kortavale.org.</p>
    <p>For consumers that do not have access to a local drop-off center, the KRT-VB sponsors a National Mail-Back Program intended for smaller quantities of EPS which can be mailed via ParcelNorth to more than 20 locations nationwide. Full instructions and a list of Mail-Back locations are available on the KRT-VB website.</p>
  </div>
  <div class="mini-brand"><span class="brand-dot"></span><span class="brand-name">Kortavale<br>Alliance</span></div>

  <div class="band orange">POST-CONSUMER EPS RECYCLING 1990-2018</div>
  <div class="band olive">DATA</div>

  <div class="photo-round photo-sorting" role="img" aria-label="Photo of a recycling facility floor with sorted white foam blocks"></div>
  <div class="photo-round photo-worker" role="img" aria-label="Photo of a worker handling a large sheet of white foam packaging"></div>
  <div class="stat industrial"><div class="label">Post-Industrial</div><div class="unit">(millions of pounds)</div><div class="value">39.0</div></div>
  <div class="stat-divider"></div>
  <div class="stat consumer"><div class="label">Post-Consumer</div><div class="unit">(millions of pounds)</div><div class="value">30.0</div></div>

  <div class="pill pill-history">
    <svg width="26" height="24" viewBox="0 0 26 24" aria-hidden="true"><path d="M3 15 L11 7 L11 11 L21 11 L21 19 L11 19 L11 23 Z" fill="none" stroke="#fff" stroke-width="1.4" stroke-linejoin="round" transform="rotate(-30 13 14)"/></svg>
    <p>The 25-year baseline shows incremental gains with more than 23 million pounds of EPS recycled annually on average. Like all commodity markets, the EPS recycling market is cyclical. The 2017 results reflect a decrease from 2016 due to the new landscape for recycling commodities and changing international markets, especially in China.</p>
  </div>

  <div class="contact-box">
    <h3>©Copyright 2018 Kortavale Alliance</h3>
    <p class="fine">The information contained herein is provided without any express or implied warranty as to its truthfulness or accuracy.<br>The Kortavale Alliance does not endorse the products or processes of any individual manufacturer or recycler.</p>
    <div class="contact-line" style="margin-top:12px">
      <svg width="9" height="12" viewBox="0 0 9 12" aria-hidden="true"><path d="M4.5 11.5 C1.5 7.5 .5 5.8 .5 4.4 A4 4 0 0 1 8.5 4.4 C8.5 5.8 7.5 7.5 4.5 11.5 Z" fill="none" stroke="var(--olive)" stroke-width="1.3"/><circle cx="4.5" cy="4.4" r="1.4" fill="var(--olive)"/></svg>
      450 Alder Park Rd., Suite 12, Brenton, MD 20650
    </div>
    <div class="contact-line phone">
      <svg width="13" height="13" viewBox="0 0 24 24" aria-hidden="true"><path d="M6.6 10.8a15 15 0 0 0 6.6 6.6l2.2-2.2a1 1 0 0 1 1-.25 11.4 11.4 0 0 0 3.6.57 1 1 0 0 1 1 1V20a1 1 0 0 1-1 1A17 17 0 0 1 3 4a1 1 0 0 1 1-1h3.5a1 1 0 0 1 1 1c0 1.25.2 2.45.57 3.57a1 1 0 0 1-.25 1z" fill="var(--olive)"/></svg>
      800-555-0142
    </div>
    <div class="contact-line"><span class="social-square"></span>kortavale.org/recycling</div>
  </div>

  <div class="column-rule"></div>
  <div class="photo-round photo-beads" role="img" aria-label="Photo of a pressed white foam surface with a recycling code"></div>
  <p class="data-text">More than 89 million pounds of EPS were recycled during calendar year 2018. This figure includes 25.9 million pounds of post-consumer packaging and 39.0 million pounds of post-industrial recovery. Post-consumer is defined as any material that is recycled after its intended end-use while post-industrial recovery includes EPS facility scrap that is recycled but never served its intended purpose as a packaging material or other end-use application.</p>
  <div class="total"><div class="caption">2018 Total<small>million pounds of EPS recycled</small></div><div class="num">89.0</div></div>

  <div class="bar-title">EPS Recycling Post-Consumer &amp; Post-Industrial<small>(millions of pounds)</small></div>
  <div class="legend consumer"><i></i>— POST-CONSUMER</div>
  <div class="legend industrial"><i></i>— POST-INDUSTRIAL</div>

  <div class="pill pill-outlook">
    <svg width="26" height="24" viewBox="0 0 26 24" aria-hidden="true"><path d="M3 15 L11 7 L11 11 L21 11 L21 19 L11 19 L11 23 Z" fill="none" stroke="#fff" stroke-width="1.4" stroke-linejoin="round" transform="rotate(-30 13 14)"/></svg>
    <p>Despite lower collection amounts reflected in 2017, EPS has historically enjoyed consistent growth since its inception in the early 1990's. This decrease is a direct result of export restrictions on recycled plastics and a reprocessing plant closure that previously recycled large quantities of EPS. Newer EPS recycling technologies to facilitate EPS collection and reprocessing launched in 2018 indicate growth rates will continue on an upward trend in the future.</p>
  </div>

  <div class="footer-tag"><b>2018</b> | EPS RECYCLING RATE REPORT</div>
</section>

</body>
</html>
```